4th Generation Family Business Needs a New Card Design!

We are a family owned 4th Generation company. We are based in the Sydney, Australia area and we are desperately in need of a more modern and classy card. We are monumental masons who design, supply & erect lasting memorials throughout cemeteries in Sydney. Our customers are normally in a period of grieving. I have attached logo files that will need to be implemented on the card. Company was established 1935. Australian Owned and Operated. Card needs to be designed to PRINTLY.com specification.

Target Market(s)

Our target market is based upon people that a grieving for family members that have passed away. We also deal with alot of companies that own and operate cemeteries.

Industry/Entity Type

Business

Contact Information for Business Card

Oliver Brantley, Operations Manager, 0417552908, oliver@hollowaystoneworks.com.au
Martin Brantley, Director, 0431906627, martin@hollowaystoneworks.com.au
Phone # 02 9634 2258
Website: www.hollowaystoneworks.com.au
Address: Suite 17, 8 Calloway Lane, East Penrose, Sydney NSW 2290

Font styles to use
Serif
Decorative
Script

Requirements
Must have
• Would like to see the logo nicely implemented with a modern design. Embossed lettering would be a nice additive.

```html
<!DOCTYPE html>
<html lang="en">
<head>
<meta charset="utf-8">
<title>Holloway Stoneworks – Business Cards</title>
<link rel="stylesheet" href="https://fonts.googleapis.com/css2?family=Open+Sans:wght@400;600&display=swap">
<style>
  :root {
    --bg: #ece9e4;
    --card-dark: #2b2a2a;
    --card-light: #ffffff;
    --gold: #e7b425;
    --ink: #2a2a2a;
    --ink-light: #f2f2f2;
    --divider: #3c3b3b;
  }
  * { box-sizing: border-box; margin: 0; padding: 0; }
  html, body { width: 1200px; height: 900px; overflow: hidden; }
  body {
    background: var(--bg);
    font-family: "Open Sans", Arial, sans-serif;
    position: relative;
  }
  .card {
    position: absolute;
    width: 580px;
    height: 340px;
    border-radius: 3px;
    box-shadow: 0 6px 18px rgba(0,0,0,.18);
  }
  .card--back {
    left: 120px; top: 150px;
    background: var(--card-dark);
    color: var(--ink-light);
  }
  .card--front {
    left: 500px; top: 410px;
    background: var(--card-light);
    color: var(--ink);
  }
  .brand-name {
    position: absolute;
    font-weight: 600;
    font-size: 27px;
    line-height: 1.15;
    letter-spacing: 1px;
    text-transform: uppercase;
    text-align: center;
  }
  .card--back .brand-name { left: 40px; top: 125px; width: 250px; color: var(--ink-light); }
  .card--front .brand-name { left: 30px; top: 125px; width: 260px; color: var(--ink); }
  .divider {
    position: absolute;
    left: 310px; top: 40px;
    width: 1px; height: 190px;
    background: var(--divider);
  }
  .contact-list { position: absolute; list-style: none; font-size: 13px; }
  .contact-list li { display: flex; align-items: flex-start; gap: 8px; margin-bottom: 4px; }
  .contact-list svg { flex: none; width: 12px; height: 12px; margin-top: 3px; fill: var(--gold); }
  .contact-list--company { left: 330px; top: 60px; }
  .contact-list--address { left: 330px; top: 150px; width: 220px; line-height: 1.4; }
  .people { position: absolute; left: 300px; top: 50px; }
  .person { margin-bottom: 16px; }
  .person__name { color: var(--gold); font-weight: 600; font-size: 17px; }
  .person__role { font-size: 13.5px; margin-bottom: 6px; }
  .person .contact-list { position: static; font-size: 13.5px; padding-left: 14px; }
</style>
</head>
<body>
  <svg width="0" height="0" style="position:absolute">
    <symbol id="icon-phone" viewBox="0 0 24 24"><path d="M6.6 10.8a15 15 0 0 0 6.6 6.6l2.2-2.2c.3-.3.7-.4 1-.2 1.1.4 2.3.6 3.6.6.6 0 1 .4 1 1V20c0 .6-.4 1-1 1C10.6 21 3 13.4 3 4c0-.6.4-1 1-1h3.5c.6 0 1 .4 1 1 0 1.2.2 2.4.6 3.6.1.3 0 .7-.2 1z"/></symbol>
    <symbol id="icon-globe" viewBox="0 0 24 24"><circle cx="12" cy="12" r="10"/></symbol>
    <symbol id="icon-pin" viewBox="0 0 24 24"><path d="M12 2a7 7 0 0 0-7 7c0 5 7 13 7 13s7-8 7-13a7 7 0 0 0-7-7zm0 9.5A2.5 2.5 0 1 1 12 6.5a2.5 2.5 0 0 1 0 5z"/></symbol>
    <symbol id="icon-mail" viewBox="0 0 24 24"><path d="M2 5h20v14H2z"/></symbol>
  </svg>

  <section class="card card--back">
    <div class="brand-name">Holloway<br>Stoneworks</div>
    <div class="divider"></div>
    <ul class="contact-list contact-list--company">
      <li><svg><use href="#icon-phone"/></svg>02 9634 2258</li>
      <li><svg><use href="#icon-globe"/></svg>www.hollowaystoneworks.com.au</li>
    </ul>
    <ul class="contact-list contact-list--address">
      <li><svg><use href="#icon-pin"/></svg>Suite 17, 8 Calloway Lane, East Penrose, Sydney NSW 2290</li>
    </ul>
  </section>

  <section class="card card--front">
    <div class="brand-name">Holloway<br>Stoneworks</div>
    <div class="people">
      <div class="person">
        <div class="person__name">Oliver Brantley</div>
        <div class="person__role">Operations Manager</div>
        <ul class="contact-list">
          <li><svg><use href="#icon-phone"/></svg>0417552908</li>
          <li><svg><use href="#icon-mail"/></svg>oliver@hollowaystoneworks.com.au</li>
        </ul>
      </div>
      <div class="person">
        <div class="person__name">Martin Brantley</div>
        <div class="person__role">Director</div>
        <ul class="contact-list">
          <li><svg><use href="#icon-phone"/></svg>0431906627</li>
          <li><svg><use href="#icon-mail"/></svg>martin@hollowaystoneworks.com.au</li>
        </ul>
      </div>
    </div>
  </section>
</body>
</html>
```